Social Media covers for a vacation rental startup

Tivvit.com is a property management company that specializes in the short-term rental of beach houses in the coast of the Arabian Gulf (aka the Persian Gulf) in Kuwait.

Tivvit.com allows users to browse through a list of beach houses and make the booking easily. The main characteristic of tivvit is simplicity. The identity of the company is based around minimalist design with no frills.

We need a to design a facebook page. I would like to use this page for google plus and Youtube.

Check out our website on tivvit.com

Target Market(s)

People looking for short term rental in Kuwait.

Typically young mothers or young men looking to spend time with their friends.

Industry/Entity Type

It Company

Colors
3176b5
85acd3
f68e4e

Requirements
Must have
• The pictures should reflect the Kuwaiti beach environment.
Nice to have
• There should be no mountains and no palm trees.
• The environment in Kuwait does not have these elements.

```html
<!DOCTYPE html>
<html lang="en">
<head>
<meta charset="utf-8">
<title>Tivvit.com – Page Cover</title>
<link href="https://fonts.googleapis.com/css2?family=Open+Sans:wght@400;600;700&family=Montserrat:wght@700&display=swap" rel="stylesheet">
<style>
  :root {
    --brand-blue: #0a8fd6;
    --brand-orange: #f68e4e;
    --ink-dark: #1f2a33;
    --page-white: #ffffff;
    --frame-grey: #c9cdd3;
    --button-grey: #f6f7f9;
    --button-text: #4b4f56;
    --photo-cool: #9fb0c4;
    --photo-warm: #b9b0a4;
  }
  * { margin: 0; padding: 0; box-sizing: border-box; }
  html, body { width: 1200px; height: 551px; overflow: hidden; background: var(--page-white); }
  .cover-canvas {
    position: relative;
    width: 1200px;
    height: 551px;
    overflow: hidden;
    background: var(--page-white);
    font-family: "Open Sans", Arial, sans-serif;
  }
  .cover-banner {
    position: absolute;
    left: 0; top: 0;
    width: 1200px; height: 470px;
    overflow: hidden;
    border-bottom: 1px solid var(--frame-grey);
  }
  .beach-photo {
    position: absolute;
    inset: 0;
    background: linear-gradient(180deg, var(--photo-cool) 0%, var(--photo-warm) 100%);
  }
  .blue-sweep {
    position: absolute;
    left: 0; top: 0;
    width: 1200px; height: 470px;
  }
  .blue-sweep .sweep-fill { fill: var(--brand-blue); }
  .blue-sweep .sweep-band { fill: var(--page-white); opacity: 0.2; }
  .cover-tagline {
    position: absolute;
    left: 19px; top: 13px;
    width: 260px;
    color: var(--page-white);
    font-family: "Montserrat", Arial, sans-serif;
    font-weight: 700;
    font-size: 20px;
    line-height: 27px;
    text-transform: uppercase;
  }
  .brand-lockup {
    position: absolute;
    left: 760px; top: 134px;
    width: 430px;
    text-align: center;
  }
  .brand-name {
    display: flex;
    align-items: center;
    justify-content: center;
    gap: 14px;
    color: var(--brand-orange);
    font-family: "Montserrat", Arial, sans-serif;
    font-weight: 700;
    font-size: 56px;
    line-height: 60px;
  }
  .brand-dot {
    width: 22px; height: 22px;
    border-radius: 50%;
    background: var(--brand-orange);
  }
  .brand-slogan {
    margin-top: 0;
    color: var(--ink-dark);
    font-size: 19px;
    font-weight: 600;
  }
  .page-actions {
    position: absolute;
    top: 410px;
    left: 800px;
    display: flex;
  }
  .action-button {
    height: 40px;
    display: flex;
    align-items: center;
    gap: 7px;
    padding: 0 14px;
    background: var(--button-grey);
    border: 1px solid var(--frame-grey);
    border-radius: 3px;
    color: var(--button-text);
    font-size: 16px;
    font-weight: 700;
  }
  .action-like { margin-right: 18px; }
  .action-follow { color: #9da2a9; font-weight: 600; border-radius: 3px 0 0 3px; }
  .action-message { border-radius: 0; border-left: none; }
  .action-more { border-radius: 0 3px 3px 0; margin-left: 4px; padding: 0 16px; }
  .action-button svg { display: block; }
  .profile-frame {
    position: absolute;
    left: 21px; top: 264px;
    width: 236px; height: 246px;
    background: var(--page-white);
    border: 1px solid var(--frame-grey);
    border-radius: 4px;
    box-shadow: 0 1px 3px rgba(0,0,0,0.25);
    padding: 5px;
  }
  .profile-frame-inner {
    width: 100%; height: 100%;
    border: 1px solid #e1e3e6;
    background: var(--page-white);
  }
</style>
</head>
<body>
<div class="cover-canvas">
  <div class="cover-banner">
    <div class="beach-photo" role="img" aria-label="Cover photo: a calm Kuwaiti beach at sunset with soft waves and a cloudy sky"></div>

    <svg class="blue-sweep" viewBox="0 0 1200 470" aria-hidden="true">
      <path class="sweep-band" d="M268,0 L395,0 C405,160 560,340 747,470 C500,380 300,200 268,0 Z"/>
      <path class="sweep-fill" d="M0,0 H268 C300,200 500,380 747,470 H0 Z"/>
    </svg>

    <p class="cover-tagline">Your subtitle or tagline</p>

    <div class="brand-lockup">
      <div class="brand-name"><span class="brand-dot"></span>Tivvit.com</div>
      <p class="brand-slogan">life is better at the beach</p>
    </div>

    <div class="page-actions">
      <div class="action-button action-like">
        <svg width="16" height="16" viewBox="0 0 16 16"><path fill="#4b4f56" d="M1 7h3v8H1zM5 7l3-6c1.2 0 2 .8 2 2v3h4c.8 0 1.4.8 1.2 1.6l-1.3 6.2c-.2.7-.8 1.2-1.5 1.2H5z"/></svg>
        Like
      </div>
      <div class="action-button action-follow">
        <svg width="12" height="12" viewBox="0 0 12 12"><path fill="#9da2a9" d="M5 0h2v5h5v2H7v5H5V7H0V5h5z"/></svg>
        Follow
      </div>
      <div class="action-button action-message">
        <svg width="16" height="15" viewBox="0 0 16 15"><path fill="#4b4f56" d="M1 1h14v10H6l-4 3v-3H1z"/></svg>
        Message
      </div>
      <div class="action-button action-more">
        <svg width="22" height="6" viewBox="0 0 22 6"><circle cx="3" cy="3" r="2.6" fill="#4b4f56"/><circle cx="11" cy="3" r="2.6" fill="#4b4f56"/><circle cx="19" cy="3" r="2.6" fill="#4b4f56"/></svg>
      </div>
    </div>
  </div>

  <div class="profile-frame"><div class="profile-frame-inner"></div></div>
</div>
</body>
</html>
```